Bright Vale Inc - Cutting-Edge Biotech Laboratory - Sleek & Sophisticated

Please design a website that has more of a high-tech and high-end feel, with contents outlined in the uploaded file.

Please have main tabs of the following categories: Home, About, FDA & LAWS, Science, Products, Media, Contact.

Media can include all the videos and photos.

Current website: www.brightvaleprime.com - it needs to be much more high-end, sleek and more organized. Please do NOT follow the outlines in the old website, but follow the uploaded CONTENT file.

Target Market(s)

doctors

Industry/Entity Type

Biotechnology

Coding

Coded - Design and coding required

Number of Pages Required

5+ page

Requirements
Must have
• Logo
Nice to have
• Some lotion on the website

```html
<!DOCTYPE html>
<html lang="en">
<head>
<meta charset="utf-8">
<title>Bright Vale Inc — Innovation in Stem Cell Therapy</title>
<link rel="stylesheet" href="https://fonts.googleapis.com/css2?family=Poppins:wght@300;400;500;600;700&display=swap">
<style>
:root{
  --navy:#1d2656;
  --lime:#8db51f;
  --ink:#222;
  --text:#555;
  --muted:#9a9a9a;
  --line:#e3e3e3;
  --grey:#f1f1f1;
  --footer:#151515;
  --white:#fff;
  --sky1:#0f5f9a;
  --sky2:#8fd2ef;
}
*{box-sizing:border-box;margin:0;padding:0}
html,body{width:1200px;height:3536px;overflow:hidden}
body{font-family:"Poppins",sans-serif;color:var(--text);background:var(--white);position:relative}
.abs{position:absolute}
/* header */
.site-header{left:0;top:0;width:1200px;height:85px;background:var(--white);border-bottom:1px solid var(--line)}
.brand{left:111px;top:0;width:155px;height:118px;background:var(--white);box-shadow:0 2px 8px rgba(0,0,0,.15);z-index:3;display:flex;flex-direction:column;align-items:center;justify-content:center;gap:10px}
.brand-dot{width:44px;height:44px;border-radius:50%;background:var(--lime)}
.brand-name{font-size:15px;font-weight:600;color:var(--navy);letter-spacing:1px}
.search{left:893px;top:10px;width:197px;height:26px;border:1px solid var(--line);font-size:10px;padding:6px 10px;color:var(--ink)}
.search-btn{right:0;top:0;width:28px;height:24px;background:#eee}
.main-nav{left:300px;top:52px;display:flex;gap:0;font-size:12px;font-weight:500;color:#444}
.main-nav a{text-decoration:none;color:inherit;width:95px;text-align:center}
.main-nav a.active{color:var(--lime)}
.phone-tab{left:960px;top:42px;width:130px;height:43px;background:var(--navy);color:var(--white);font-size:15px;display:flex;align-items:center;justify-content:center;gap:8px}
/* hero */
.hero{left:0;top:85px;width:1200px;height:481px;background:linear-gradient(120deg,var(--sky1) 0%,#3a97cc 35%,#d6e9f3 70%,#eef3f6 100%)}
.hero-box{left:224px;top:207px;width:766px;height:264px;background:rgba(255,255,255,.55);text-align:center}
.hero-title{margin-top:58px;font-size:34px;font-weight:700;color:#111;letter-spacing:.5px}
.hero-sub{font-size:15px;color:var(--navy);margin-top:2px}
.btn{display:inline-block;background:var(--navy);color:var(--white);font-weight:500;text-align:center}
.hero-btn{left:490px;top:354px;width:217px;height:58px;line-height:58px;font-size:14px}
/* services */
.services-panel{left:111px;top:566px;width:979px;height:480px;background:var(--white)}
.service{width:160px;height:160px;border-radius:50%;background:#ececec;border:6px solid var(--white);box-shadow:0 2px 8px rgba(0,0,0,.15);top:528px;display:flex;flex-direction:column;align-items:center;justify-content:flex-end;padding-bottom:36px;font-size:12px;font-weight:500;color:#c9c9c9;text-transform:uppercase;text-align:center;line-height:1.2}
.service svg{margin-bottom:10px}
.service.active{background:var(--lime);color:var(--white)}
.intro{left:130px;top:728px;width:940px;font-size:11.5px;line-height:25px;text-align:center}
.intro p{margin-bottom:10px}
.small-btn{height:34px;line-height:34px;font-size:11px;font-weight:600}
/* video */
.video-band{left:0;top:1080px;width:1200px;height:523px;background:linear-gradient(90deg,#eaeaea,#dcdcdc 60%,#d2d2d2)}
.section-left-title{left:111px;top:1148px;font-size:29px;font-weight:500;color:var(--navy)}
.video-meta{left:111px;top:1188px;font-size:14px;color:var(--navy);line-height:20px}
.video-meta b{font-weight:600}
.video-copy{left:111px;top:1244px;width:340px;font-size:11.5px;line-height:28px}
.video-frame{left:549px;top:1150px;width:541px;height:377px;background:linear-gradient(135deg,#8a8168,#c9c2ae 45%,#6e6a5c);box-shadow:0 3px 10px rgba(0,0,0,.25)}
.video-bar{left:0;bottom:0;width:100%;height:26px;background:rgba(0,0,0,.7)}
.video-icon{right:10px;width:30px;height:30px;background:#222;border-radius:3px}
/* headings */
.section-title{left:0;width:1200px;text-align:center;font-size:30px;font-weight:500;color:var(--navy)}
.section-copy{left:120px;width:960px;text-align:center;font-size:11.5px;line-height:28px}
/* products */
.product{top:1808px;width:292px;height:342px;background:var(--white);box-shadow:0 4px 14px rgba(0,0,0,.2)}
.product-photo{left:0;top:0;width:100%;height:257px;background:linear-gradient(90deg,#9d9c98,#d8d8d6 50%,#a5a4a0)}
.product-name{left:0;top:265px;width:100%;text-align:center;font-size:14px;color:var(--text)}
.product-price{left:0;top:290px;width:100%;text-align:center;font-size:24px;font-weight:600;color:var(--navy)}
/* testimonials */
.testimonials{left:0;top:2227px;width:1200px;height:432px;background:var(--grey)}
.quote{left:300px;top:2362px;width:600px;text-align:center;font-size:12px;font-style:italic;line-height:28px;color:#444}
.avatar{left:549px;top:2463px;width:104px;height:104px;border-radius:50%;border:5px solid var(--lime);background:linear-gradient(180deg,#c9a98a,#8a6a55)}
.patient{left:0;top:2575px;width:1200px;text-align:center;font-size:12px;color:#444}
/* contact */
.field{height:47px;border:1px solid var(--line);font-size:11px;color:var(--muted);padding:15px 16px}
/* social */
.social{left:490px;top:3207px;display:flex;gap:14px}
.social span{width:36px;height:36px;border-radius:50%;background:var(--white);border:1px solid #ddd;display:block}
/* footer */
.site-footer{left:0;top:3225px;width:1200px;height:311px;background:var(--footer);color:#bbb}
.footer-title{top:3276px;font-size:21px;color:#eaeaea}
.footer-rule{top:3316px;height:1px;background:#444}
.quick-links{left:111px;top:3326px;list-style:none;font-size:11px;line-height:19.5px}
.quick-links li::before{content:"›";margin-right:10px}
.contact-list{left:346px;top:3322px;font-size:12px;line-height:20px;width:230px}
.contact-list div{display:flex;gap:10px;margin-bottom:10px}
.map{left:594px;top:3323px;width:224px;height:118px;background:linear-gradient(135deg,#d9e7c9,#bcd4e8 55%,#e8e3d3)}
.news-copy{left:874px;top:3322px;width:215px;font-size:11px;line-height:17px}
.news-input{left:874px;top:3364px;width:215px;height:36px;background:var(--white);color:#777;font-size:11px;padding:11px 10px}
.news-btn{left:874px;top:3407px;width:101px;height:34px;line-height:34px;font-size:11px}
.copyright{left:0;top:3497px;width:1200px;text-align:center;font-size:11px;color:#aaa}
</style>
</head>
<body>

<header class="site-header abs">
  <div class="search abs">SEARCH<span class="search-btn abs"></span></div>
  <nav class="main-nav abs">
    <a class="active">HOME</a><a>ABOUT</a><a>FDA &amp; LAWS</a><a>SCIENCE</a><a>PRODUCTS</a><a>CONTACT</a>
  </nav>
  <div class="phone-tab abs">
    <svg width="14" height="14" viewBox="0 0 24 24"><path fill="#fff" d="M6.6 10.8a15 15 0 0 0 6.6 6.6l2.2-2.2a1 1 0 0 1 1-.25 11.4 11.4 0 0 0 3.6.6 1 1 0 0 1 1 1V20a1 1 0 0 1-1 1A17 17 0 0 1 3 4a1 1 0 0 1 1-1h3.5a1 1 0 0 1 1 1c0 1.25.2 2.45.6 3.6a1 1 0 0 1-.25 1z"/></svg>
    5550142870
  </div>
</header>
<div class="brand abs"><span class="brand-dot"></span><span class="brand-name">BRIGHT VALE</span></div>

<section class="hero abs" role="img" aria-label="Scientist in a laboratory holding a test tube against a blue cellular background"></section>
<div class="hero-box abs">
  <h1 class="hero-title">INNOVATION IN STEM CELL THERAPY</h1>
  <p class="hero-sub">Leader In Regenerative Medicine Innovator Of The Industry</p>
</div>
<a class="btn hero-btn abs">LEARN MORE</a>

<section class="services-panel abs"></section>
<div class="service active abs" style="left:125px">
  <svg width="44" height="54" viewBox="0 0 44 54" fill="none" stroke="#fff" stroke-width="3"><path d="M14 4v20l8 6v20M30 4v16l-8 10"/><circle cx="22" cy="30" r="4"/></svg>ORTHOPEDICS</div>
<div class="service abs" style="left:321px">
  <svg width="44" height="44" viewBox="0 0 44 44" fill="none" stroke="#d0d0d0" stroke-width="3"><ellipse cx="22" cy="22" rx="18" ry="11" transform="rotate(-40 22 22)"/><path d="M16 28l12-12"/></svg>SPORTS MEDICINE</div>
<div class="service abs" style="left:516px">
  <svg width="44" height="44" viewBox="0 0 44 44" fill="none" stroke="#d0d0d0" stroke-width="3"><ellipse cx="14" cy="26" rx="6" ry="13"/><ellipse cx="30" cy="26" rx="6" ry="13"/></svg>WOUND CARE</div>
<div class="service abs" style="left:712px">
  <svg width="44" height="44" viewBox="0 0 44 44" fill="none" stroke="#d0d0d0" stroke-width="3"><rect x="4" y="16" width="36" height="12" rx="6" transform="rotate(45 22 22)"/><rect x="4" y="16" width="36" height="12" rx="6" transform="rotate(-45 22 22)"/></svg>PODIATRY</div>
<div class="service abs" style="left:908px">
  <svg width="44" height="44" viewBox="0 0 44 44" fill="none" stroke="#d0d0d0" stroke-width="3"><circle cx="22" cy="10" r="5"/><path d="M6 32h32M10 32l6-12h12l6 12"/></svg>PAIN<br>MANAGEMENT</div>

<div class="intro abs">
  <p>Bright Vale Cell Therapy provides Embryonic Stem Cells and unique protocols to doctors in order to help their patients who face major health conditions as well as individuals who simply wish to stay young and healthy. Over the past five years of development, we have successfully conducted research into targeted major diseases related to kidney, liver and heart failures, we have aided in helping people who have suffered stroke or brain injury to walk or talk again, we have removed all traces of tumor in multiple cancer patients and we have achieved significant results in fighting aging and its physical markers.</p>
  <p>BVCT has developed innovative processes and safety protocols, which deliver the highest cellular tissue viability and safety standards. With these safety and quality standards, BVCT will become the leader of amniotic membrane tissue allografts in the field of regenerative medicine.</p>
  <p>The BVCT proprietary process preserves the integrity of the amnion tissue, achieving greater clinical outcomes. This unique process yields high concentrations of tissue, growth factors, anti-inflammatory cytokines, and is chorion free. Our products contain these extracellular proteins and molecules which induce soft tissue healing, reduce scar tissue, and promote tissue regeneration.</p>
</div>
<a class="btn small-btn abs" style="left:556px;top:997px;width:104px">READ MORE</a>

<section class="video-band abs" role="img" aria-label="Soft blurred medical background with a stethoscope"></section>
<h2 class="section-left-title abs">WATCH OUR VIDEO</h2>
<p class="video-meta abs">Interview With Company Owner <b>Daniel Marsh</b><br>On Stem Cells</p>
<p class="video-copy abs">The BVCT proprietary process preserves the integrity of the amnion tissue, achieving greater clinical outcomes. This unique process yields high concentrations of tissue, growth factor anti-inflammatory cytokines, and is chorion free. Our products contain these extracellular proteins and molecules which induce.</p>
<div class="video-frame abs" role="img" aria-label="Video still of an interview in a bright studio">
  <span class="video-icon abs" style="top:14px"></span>
  <span class="video-icon abs" style="top:50px"></span>
  <div class="video-bar abs"></div>
</div>

<h2 class="section-title abs" style="top:1665px">OUR PRODUCTS</h2>
<p class="section-copy abs" style="top:1712px">The BVCT proprietary process preserves the integrity of the amnion tissue, achieving greater clinical outcomes. This unique process yields high concentrations of tissue, growth factor anti-inflammatory cytokines, and is chorion free. Our products contain these extracellular proteins and molecules which induce.</p>
<article class="product abs" style="left:111px"><div class="product-photo abs" role="img" aria-label="Silver tube of rejuvenating repairing cream"></div><p class="product-name abs">Rejuvenating Repairing Cream</p><p class="product-price abs">$300.00</p></article>
<article class="product abs" style="left:455px"><div class="product-photo abs" role="img" aria-label="Silver tube of rejuvenating repairing cream"></div><p class="product-name abs">Rejuvenating Repairing Cream</p><p class="product-price abs">$300.00</p></article>
<article class="product abs" style="left:798px"><div class="product-photo abs" role="img" aria-label="Silver tube of rejuvenating repairing cream"></div><p class="product-name abs">Rejuvenating Repairing Cream</p><p class="product-price abs">$300.00</p></article>

<section class="testimonials abs"></section>
<h2 class="section-title abs" style="top:2287px">TESTIMONIALS</h2>
<svg class="abs" style="left:112px;top:2420px" width="30" height="60" viewBox="0 0 30 60"><path d="M26 2L4 30l22 28" fill="none" stroke="#d6d6d6" stroke-width="2"/></svg>
<svg class="abs" style="left:1058px;top:2420px" width="30" height="60" viewBox="0 0 30 60"><path d="M4 2l22 28L4 58" fill="none" stroke="#d6d6d6" stroke-width="2"/></svg>
<p class="quote abs"><span style="color:#ccc;font-size:22px">❝</span> Bright Vale Cell Therapy provides Embryonic Stem Cells and unique protocols to doctors in order to help their patients who face major health conditions as well as individuals who simply wish to stay young and healthy. Over the past five years of development. <span style="color:#ccc;font-size:22px">❞</span></p>
<div class="avatar abs" role="img" aria-label="Portrait of a patient"></div>
<p class="patient abs">Miss. Patient Name</p>

<h2 class="section-title abs" style="top:2716px">CONTACT US</h2>
<p class="section-copy abs" style="top:2765px">The BVCT proprietary process preserves the integrity of the amnion tissue, achieving greater clinical outcomes. This unique process yields high concentrations</p>
<div class="field abs" style="left:160px;top:2826px;width:432px">First Name</div>
<div class="field abs" style="left:608px;top:2826px;width:432px">Last Name</div>
<div class="field abs" style="left:160px;top:2887px;width:432px">Email</div>
<div class="field abs" style="left:608px;top:2887px;width:432px">Contact</div>
<div class="field abs" style="left:160px;top:2949px;width:880px;height:106px">Text Message</div>
<a class="btn small-btn abs" style="left:549px;top:3107px;width:102px">SEND</a>

<footer class="site-footer abs"></footer>
<div class="social abs"><span></span><span></span><span></span><span></span><span></span></div>

<h3 class="footer-title abs" style="left:111px">Quick Links</h3>
<div class="footer-rule abs" style="left:111px;width:160px"></div>
<ul class="quick-links abs"><li>Home</li><li>About</li><li>Fda &amp; Laws</li><li>Science</li><li>Products</li><li>Contact</li></ul>

<h3 class="footer-title abs" style="left:346px">Contact Detail</h3>
<div class="footer-rule abs" style="left:346px;width:230px"></div>
<div class="contact-list abs">
  <div><svg width="14" height="18" viewBox="0 0 14 18"><path fill="#fff" d="M7 0a7 7 0 0 0-7 7c0 5 7 11 7 11s7-6 7-11a7 7 0 0 0-7-7zm0 9.5A2.5 2.5 0 1 1 7 4.5a2.5 2.5 0 0 1 0 5z"/></svg><span>Bright Vale Cell Therapy, 1200 Harbor Lane, Westfield, MI 48300</span></div>
  <div><svg width="14" height="14" viewBox="0 0 24 24"><path fill="#fff" d="M6.6 10.8a15 15 0 0 0 6.6 6.6l2.2-2.2a1 1 0 0 1 1-.25 11.4 11.4 0 0 0 3.6.6 1 1 0 0 1 1 1V20a1 1 0 0 1-1 1A17 17 0 0 1 3 4a1 1 0 0 1 1-1h3.5a1 1 0 0 1 1 1c0 1.25.2 2.45.6 3.6a1 1 0 0 1-.25 1z"/></svg><span style="font-size:14px">5550142870</span></div>
  <div><svg width="14" height="12" viewBox="0 0 14 12"><rect x="0.5" y="0.5" width="13" height="11" fill="#fff"/><path d="M1 1l6 5 6-5" fill="none" stroke="#151515"/></svg><span style="font-size:11px">info@brightvaleprime.com</span></div>
</div>
<div class="map abs" role="img" aria-label="Location map"></div>

<h3 class="footer-title abs" style="left:874px">Newsletter Sign Up</h3>
<p class="news-copy abs">Stay connected and receive email updates from Us</p>
<div class="news-input abs">Enter your email here</div>
<a class="btn news-btn abs">SUBSCRIBE</a>

<div class="abs" style="left:0;top:3477px;width:1200px;height:1px;background:#333"></div>
<p class="copyright abs">Copyright © 2018 BRIGHTVALEPRIME . All Rights Reserved</p>

</body>
</html>
```